New look and feel for Kestrel Sound

We need landing page designs for our company that manufactures high end bass guitars and related electronic products. We will be using premier musicians to promote the product on the site. We have recently designed a new logo, which is in the upload files. A link to our Pinwheel page is at www.kestrelsound.example

Target Market(s)

Professional Musicians and serious Amateurs

Industry/Entity Type

Electronic

Number of Pages Required

5+ page

Font styles to use
Serif

Requirements
Must have
• Utilize images of product and endorsing musicians to promote drive interest
Should not have
• Anything that is outer space or "alien" looking

```html
<!DOCTYPE html>
<html lang="en">
<head>
<meta charset="utf-8">
<title>Kestrel Sound — Hand Built Bass Guitars</title>
<link rel="stylesheet" href="https://fonts.googleapis.com/css2?family=Playfair+Display:wght@400;700&family=Open+Sans:wght@400;600;700&family=Great+Vibes&display=swap">
<style>
:root{
  --gold:#c9a24a;
  --gold-light:#e0bf6e;
  --gold-band:#b8923f;
  --ink:#1b1b1b;
  --dark:#171717;
  --darker:#0e0e0e;
  --panel:#222;
  --text:#5c5c5c;
  --muted:#9a9a9a;
  --white:#ffffff;
  --paper:#f4f4f4;
}
*{box-sizing:border-box;margin:0;padding:0}
html,body{width:1200px;height:2836px;overflow:hidden}
body{font-family:"Open Sans",Arial,sans-serif;color:var(--text);background:var(--darker);font-size:13px;line-height:1.6}
.serif{font-family:"Playfair Display",Georgia,serif}
.script{font-family:"Great Vibes",cursive;color:var(--gold);font-weight:400;text-transform:none}

/* hero */
.hero{position:relative;height:480px;background:linear-gradient(110deg,#2a2420 0%,#5a4330 35%,#8b6a45 55%,#3a2d22 80%,#141210 100%);overflow:hidden}
.hero-photo{position:absolute;inset:0;background:radial-gradient(ellipse at 55% 45%,rgba(225,190,140,.45),rgba(0,0,0,0) 55%),linear-gradient(180deg,rgba(0,0,0,.25),rgba(0,0,0,.55))}
.topbar{position:absolute;top:0;left:0;right:0;height:80px;display:flex;align-items:center;padding:0 60px;background:rgba(0,0,0,.45)}
.brand{display:flex;align-items:center;gap:12px}
.brand-dot{width:38px;height:38px;border-radius:50%;background:var(--gold)}
.brand-name{font-family:"Playfair Display",Georgia,serif;font-size:22px;color:var(--gold-light);font-weight:700}
.nav{margin-left:auto;display:flex;gap:26px}
.nav a{color:var(--white);font-size:11px;font-weight:600;letter-spacing:1px;text-decoration:none}
.nav a.active{color:var(--gold-light)}
.hero-copy{position:absolute;left:0;right:0;top:340px;text-align:center;color:var(--white)}
.hero-copy h1{font-family:"Playfair Display",Georgia,serif;font-weight:400;font-size:30px;line-height:1.25}
.hero-copy h1 em{font-style:normal;color:var(--gold-light)}
.hero-copy p{font-size:12px;color:#ddd;margin-top:8px}

/* welcome */
.welcome{height:380px;background:var(--white);position:relative;padding:50px 60px 0}
.welcome h2{font-size:30px;color:var(--ink);font-weight:400}
.welcome h2 .script{font-size:40px;margin-right:8px}
.welcome-text{width:640px;margin-top:16px;font-size:11px;line-height:1.75}
.welcome-text p{margin-bottom:10px}
.btn-gold{display:inline-block;background:var(--gold);color:var(--white);font-size:10px;font-weight:700;letter-spacing:1px;padding:7px 16px;margin-top:4px}
.welcome-guitar{position:absolute;right:150px;top:40px;width:200px;height:300px;border-radius:90px 90px 110px 110px;background:radial-gradient(circle at 50% 65%,#f1d39a 0%,#b07a3c 40%,#2d1a0f 75%)}
.read-link{position:absolute;right:170px;bottom:26px;font-size:10px;color:var(--gold)}

/* guitars */
.guitars{height:840px;background:var(--dark);padding-top:60px;text-align:center}
.section-title{font-size:34px;color:var(--white);letter-spacing:2px;font-weight:400}
.section-title .script{font-size:34px;margin-right:6px}
.rule{width:120px;height:1px;background:var(--gold);margin:12px auto 40px}
.guitar-grid{width:664px;margin:0 auto;display:grid;grid-template-columns:repeat(3,208px);gap:20px 20px}
.guitar-card .thumb{height:200px;border-radius:2px}
.guitar-card h3{font-family:"Playfair Display",Georgia,serif;font-size:15px;color:var(--gold-light);font-weight:400;margin-top:10px}
.guitar-card p{font-size:10px;color:var(--muted);line-height:1.5;padding:2px 10px 0}
.t1{background:linear-gradient(135deg,#e9c38a,#a8652f)}
.t2{background:radial-gradient(circle at 50% 50%,#3c2414 20%,#c58a4b 60%,#7c4a22)}
.t3{background:linear-gradient(160deg,#d9b483,#8d5a2b)}
.t4{background:linear-gradient(120deg,#e5c08c,#5a3418)}
.t5{background:linear-gradient(150deg,#3b2a1e,#c99457 60%,#2a1c12)}
.t6{background:linear-gradient(140deg,#f0d3a4,#9b6a3b)}

/* specialty */
.specialty{height:400px;position:relative;text-align:center;padding-top:50px;background:radial-gradient(ellipse at 50% 60%,#3a2e22 0%,#141210 70%)}
.spec-row{display:flex;justify-content:center;gap:40px;margin-top:-6px}
.spec-item{width:180px}
.spec-item svg{width:36px;height:36px}
.spec-item h4{color:var(--white);font-size:11px;font-weight:700;letter-spacing:1px;margin:8px 0 6px}
.spec-item p{font-size:10px;color:var(--muted);line-height:1.5}
.specialty .btn-gold{margin-top:26px}

/* testimonial */
.testimonial{height:408px;background:var(--white);padding-top:46px;position:relative}
.testimonial .section-title{color:var(--ink)}
.title-rule{display:flex;align-items:center;justify-content:center;gap:20px}
.title-rule span{width:200px;height:1px;background:#bbb}
.quote{position:absolute;left:220px;top:140px;width:500px}
.quote blockquote{font-family:"Playfair Display",Georgia,serif;font-size:24px;color:var(--ink);font-style:italic}
.quote p{font-size:11px;margin-top:12px;line-height:1.7}
.quote .who{margin-top:14px;text-align:right;font-size:11px;color:var(--ink);font-weight:700}
.quote .who small{display:block;font-weight:400;color:var(--muted)}
.socials{display:flex;gap:6px;justify-content:flex-end;margin-top:8px}
.socials i{width:16px;height:16px;background:var(--gold)}
.artist-photo{position:absolute;right:220px;top:130px;width:220px;height:250px;background:linear-gradient(180deg,#4a4a4a,#151515)}

/* gold band */
.band{height:112px;background:var(--gold-band);display:flex;justify-content:center;gap:50px;align-items:center}
.band-item{display:flex;gap:12px;width:240px;align-items:flex-start}
.band-item i{flex:none;width:32px;height:32px;border:2px solid var(--white)}
.band-item h5{color:var(--white);font-size:11px;letter-spacing:1px}
.band-item p{font-size:9.5px;color:#f6ead0;line-height:1.45}

/* footer */
.footer{height:100px;background:var(--dark);display:flex;align-items:center;padding:0 60px;gap:40px;color:#ccc}
.footer .col1 h6{font-size:12px;color:var(--white);letter-spacing:1px}
.footer .col1 p{font-size:10px}
.subscribe{display:flex}
.subscribe span{display:block;width:200px;height:30px;background:#fff}
.subscribe b{background:var(--gold);color:#fff;font-size:10px;padding:8px 12px}
.touch{margin-left:auto;display:flex;align-items:center;gap:10px}
.touch h6{color:var(--white);font-size:11px;letter-spacing:1px}
.touch i{width:22px;height:22px;background:var(--gold)}
.bottom{height:116px;background:var(--darker);display:flex;align-items:center;padding:0 60px;gap:40px;color:var(--muted);font-size:10px}
.bottom .info b{color:var(--white)}
.bottom .links{margin-left:auto;display:flex;gap:20px}
</style>
</head>
<body>

<header class="hero">
  <div class="hero-photo" role="img" aria-label="Close-up photograph of hands playing an acoustic guitar"></div>
  <div class="topbar">
    <div class="brand"><span class="brand-dot"></span><span class="brand-name">Kestrel Sound</span></div>
    <nav class="nav"><a class="active">HOME</a><a>ABOUT US</a><a>BASSES</a><a>PREAMPS</a><a>ARTISTS</a><a>PRODUCTS</a><a>CONTACT</a></nav>
  </div>
  <div class="hero-copy">
    <h1>The finest <em>Guitar</em> hand built In The World<br>to your <em>Specifications</em> without compromise</h1>
    <p>Custom basses hand built by master luthiers for working players and collectors.<br>Hear the difference a crafted instrument makes on every stage.</p>
  </div>
</header>

<section class="welcome">
  <h2 class="serif"><span class="script">Welcome</span>to KESTREL SOUND</h2>
  <div class="welcome-text">
    <p>Every instrument we make begins with carefully chosen tonewoods, aged and matched by hand in our workshop before a single cut is made.</p>
    <p>Our builders shape each neck and body to the player, fitting frets, electronics and hardware so the bass feels right from the very first note you play.</p>
    <p>From boutique preamps to full custom orders, we work with professional musicians and serious amateurs who want an instrument built for a lifetime of playing.</p>
  </div>
  <span class="btn-gold">READ MORE</span>
  <div class="welcome-guitar" role="img" aria-label="Photograph of a sunburst acoustic bass guitar"></div>
  <span class="read-link">Click to read more</span>
</section>

<section class="guitars">
  <h2 class="section-title serif"><span class="script">Our</span>GUITARS</h2>
  <div class="rule"></div>
  <div class="guitar-grid">
    <div class="guitar-card"><div class="thumb t1" role="img" aria-label="Photograph of an electric guitar body"></div><h3>Electric Guitars</h3><p>Solid bodies voiced for punch, clarity and long sustain.</p></div>
    <div class="guitar-card"><div class="thumb t2" role="img" aria-label="Photograph of an archtop guitar soundhole"></div><h3>Archtop Guitars</h3><p>Carved tops with warm, rich voices for jazz players.</p></div>
    <div class="guitar-card"><div class="thumb t3" role="img" aria-label="Photograph of an acoustic guitar neck"></div><h3>Acoustic Guitars</h3><p>Resonant hand braced tops with a full, open tone.</p></div>
    <div class="guitar-card"><div class="thumb t4" role="img" aria-label="Photograph of an archtop guitar bridge"></div><h3>Archtop Guitars</h3><p>Classic archtop builds finished to your specification.</p></div>
    <div class="guitar-card"><div class="thumb t5" role="img" aria-label="Photograph of an acoustic guitar headstock"></div><h3>Acoustic Guitars</h3><p>Select tonewoods matched by ear for balanced response.</p></div>
    <div class="guitar-card"><div class="thumb t6" role="img" aria-label="Photograph of an electric guitar bridge"></div><h3>Electric Guitars</h3><p>Custom pickups and wiring tuned to your playing style.</p></div>
  </div>
</section>

<section class="specialty" role="region" aria-label="Specialty section over a dim guitar workshop photograph">
  <h2 class="section-title serif"><span class="script">Our</span>SPECIALTY</h2>
  <div class="rule"></div>
  <div class="spec-row">
    <div class="spec-item">
      <svg viewBox="0 0 36 36" fill="var(--gold)"><path d="M14 6l16-4v22a4 4 0 1 1-3-3.9V8l-10 2.5V27a4 4 0 1 1-3-3.9z"/></svg>
      <h4>WHY KESTREL SOUND</h4><p>Decades of craft in every instrument we release.</p>
    </div>
    <div class="spec-item">
      <svg viewBox="0 0 36 36" fill="var(--gold)"><path d="M18 2l14 5v10c0 9-6 15-14 17C10 32 4 26 4 17V7z"/></svg>
      <h4>HOW WE MAKE GUITARS</h4><p>Hand shaped, hand finished and set up by ear.</p>
    </div>
    <div class="spec-item">
      <svg viewBox="0 0 36 36" fill="none" stroke="var(--gold)" stroke-width="2.5"><rect x="12" y="3" width="12" height="20" rx="6"/><path d="M7 17a11 11 0 0 0 22 0M18 28v5M12 33h12"/></svg>
      <h4>RECREATING THE SOUND</h4><p>Vintage tones rebuilt with modern electronics.</p>
    </div>
    <div class="spec-item">
      <svg viewBox="0 0 36 36" fill="none" stroke="var(--gold)" stroke-width="2.5"><path d="M3 5h5l4 18h17l3-12H10"/><circle cx="14" cy="29" r="2.5" fill="var(--gold)"/><circle cx="27" cy="29" r="2.5" fill="var(--gold)"/></svg>
      <h4>ORDER A GUITAR</h4><p>Start your custom build with our team today.</p>
    </div>
  </div>
  <span class="btn-gold">CLICK HERE FOR MORE DETAILS</span>
</section>

<section class="testimonial">
  <div class="title-rule"><span></span><h2 class="section-title serif"><span class="script">Client</span>TESTIMONIAL</h2><span></span></div>
  <div class="quote">
    <blockquote>“The best instrument I have ever played.”</blockquote>
    <p>From the first rehearsal it was clear this bass was something special. The neck feels effortless, the tone sits perfectly in the mix, and it has never let me down on tour.</p>
    <p>I have owned many basses over the years, but this is the one I reach for every night.</p>
    <div class="who">Dale Morrow<small>Session and touring bassist</small></div>
    <div class="socials"><i></i><i></i><i></i></div>
  </div>
  <div class="artist-photo" role="img" aria-label="Photograph of an endorsing musician on stage holding a bass guitar"></div>
</section>

<section class="band">
  <div class="band-item"><i></i><div><h5>AVAILABLE NOW</h5><p>Ready to play instruments in stock and shipping this week.</p></div></div>
  <div class="band-item"><i></i><div><h5>GUITAR MAKING</h5><p>See how each bass is built by hand in our workshop.</p></div></div>
  <div class="band-item"><i></i><div><h5>CUSTOM GUITARS</h5><p>Choose woods, finish and electronics to suit you.</p></div></div>
</section>

<footer class="footer">
  <div class="col1"><h6>KESTREL SOUND</h6><p>(555) 010 4821 · (555) 010 4822</p></div>
  <div class="subscribe"><span></span><b>SUBSCRIBE</b></div>
  <div class="touch"><h6>GET IN TOUCH WITH US</h6><i></i><i></i><i></i><i></i></div>
</footer>
<div class="bottom">
  <div class="brand"><span class="brand-dot"></span><span class="brand-name">Kestrel Sound</span></div>
  <div class="info"><b>Address:</b> 42 Harbor Lane, Suite 7, Millbrook<br><b>Email:</b> hello@kestrelsound.example · www.kestrelsound.example</div>
  <div class="links"><span>Privacy Policy</span><span>Terms &amp; Conditions</span><span>© 2024 Kestrel Sound</span></div>
</div>

</body>
</html>
```